Flyer for an online formula one racing league

Hello.

I am looking for the perfect one page facebook/instagram style flyer for an online formula one racing league. The racing league is called 'VOLTA RACING LEAGUE'.

Information that MUST be on the new flyer is already on the old flyer I have uploaded here. In addition to including: The Volta racing league 'V' logo I have uploaded AND the text: 'Very popular, clean and competitive racing league, running for its 4th season. Why not join with a friend? Race times, Mondays, Tuesdays and Wednesdays each at 8pm UK TIME Message below for any questions. (Spacing of information is not important, however all the information in regards to the racing I have just mentioned MUST BE on the flyer, this includes info from old pic, logo and the other info I just mentioned).

It would be beneficial to have lots of dark blue on the flyer and the new flyer to be a lot different to the original flyer I uploaded, but this is not essential.

I apologise if I did not explain very well, any questions, please message me.

The best flyer should look the most attractive to someone that might be interested in joining an online formula one racing league.

I used this website before to create the perfect logo for my Sunday League team last year, and I was very impressed. I look forward to seeing your submissions.

Target Market(s)

No specific target, more something that may attract someone into joining a formula one online racing league

Industry/Entity Type

e sports/formula one

Colors
0054AA
0677BA
7BADD7
CADEEF
E8F1F8

Requirements
Must have
• Read product description please
Should not have
• Ignoring product description!

```html
<!DOCTYPE html>
<html lang="en">
<head>
<meta charset="utf-8">
<title>Volta Racing League – New Season</title>
<link rel="stylesheet" href="https://fonts.googleapis.com/css2?family=Russo+One&family=Saira:ital,wght@1,800&family=Montserrat:wght@800&family=Anton&family=Passion+One:wght@700&display=swap">
<style>
  :root{
    --navy-deep:#040c26;
    --navy:#0a1f55;
    --navy-mid:#12306f;
    --gold-light:#fff6a8;
    --gold:#ffd21c;
    --gold-dark:#b07a00;
    --copper-light:#ffd2b0;
    --copper:#e0703e;
    --copper-dark:#7a2a12;
    --yellow:#f5ef00;
    --red:#ff1414;
    --white:#ffffff;
    --asphalt:#3b4350;
    --asphalt-dark:#1c222c;
  }
  *{margin:0;padding:0;box-sizing:border-box}
  html,body{width:1200px;height:1200px;overflow:hidden;background:var(--navy-deep)}
  .flyer{
    position:relative;width:1200px;height:1200px;overflow:hidden;
    background:radial-gradient(ellipse at 60% 40%, var(--navy-mid) 0%, var(--navy) 45%, var(--navy-deep) 100%);
  }
  .hero-graphic{
    position:absolute;left:0;top:0;width:1200px;height:520px;
    background:
      radial-gradient(circle at 200px 248px, rgba(200,40,90,.28) 0%, rgba(10,31,85,0) 38%),
      linear-gradient(160deg, rgba(120,150,200,.35) 0%, rgba(40,70,140,.2) 35%, rgba(10,31,85,0) 65%);
  }
  .track-scene{
    position:absolute;left:0;top:820px;width:1200px;height:380px;
    background:linear-gradient(180deg, rgba(10,31,85,0) 0%, rgba(120,40,70,.35) 12%, rgba(30,40,60,.6) 30%, var(--asphalt) 60%, var(--asphalt-dark) 100%);
  }
  .brand-mark{
    position:absolute;left:62px;top:110px;width:276px;height:276px;border-radius:50%;
    background:var(--navy-deep);border:4px solid var(--white);
    display:flex;align-items:center;justify-content:center;
  }
  .brand-name{font-family:"Montserrat",sans-serif;font-weight:800;font-size:56px;color:var(--white);letter-spacing:2px}
  .title{
    position:absolute;left:400px;top:62px;width:760px;text-align:center;
    font-family:"Russo One",sans-serif;text-transform:uppercase;line-height:.84;font-weight:400;
  }
  .title span{display:block}
  .title b{
    display:inline-block;font-weight:400;
    background:linear-gradient(180deg,var(--gold-light) 0%,var(--gold) 45%,var(--gold-dark) 55%,var(--gold) 100%);
    -webkit-background-clip:text;background-clip:text;color:transparent;
    filter:drop-shadow(4px 5px 0 #3a2600);
  }
  .title .line-1{font-size:110px}
  .title .line-1 b{transform:skewX(-14deg)}
  .title .line-2{font-size:150px}
  .title .line-2 b{transform:skewX(-14deg) scaleX(1.2)}
  .title .line-3{font-size:120px}
  .title .line-3 b{transform:skewX(-14deg) scaleX(1.15)}
  .season{position:absolute;left:0;width:1200px;text-align:center}
  .season-kicker{
    top:452px;left:10px;font-family:"Saira",sans-serif;font-style:italic;font-weight:800;
    font-size:66px;color:var(--white);letter-spacing:2px;
  }
  .season-headline{
    top:525px;left:10px;font-family:"Russo One",sans-serif;font-size:100px;
    background:linear-gradient(180deg,var(--copper-light) 0%,var(--copper) 50%,var(--copper-dark) 100%);
    -webkit-background-clip:text;background-clip:text;color:transparent;
    filter:drop-shadow(3px 4px 0 #2a0800);
  }
  .pitch{
    position:absolute;left:0;top:684px;width:1180px;text-align:center;
    font-family:"Montserrat",sans-serif;font-weight:800;font-size:27px;line-height:40px;color:var(--yellow);
  }
  .invite{
    position:absolute;left:0;top:866px;width:1200px;display:flex;align-items:center;justify-content:center;gap:26px;
  }
  .invite-text{
    font-family:"Passion One",sans-serif;font-weight:700;font-size:56px;color:var(--red);
    -webkit-text-stroke:2px var(--white);paint-order:stroke fill;letter-spacing:.5px;
  }
  .chevrons{width:84px;height:34px}
  .race-times{
    position:absolute;left:0;top:946px;width:1170px;text-align:center;
    font-family:"Anton",sans-serif;font-size:56px;line-height:64px;color:var(--white);
    letter-spacing:1px;text-shadow:3px 4px 0 rgba(0,0,0,.7);
  }
  .contact-note{
    position:absolute;left:0;top:1148px;width:1170px;text-align:center;
    font-family:"Montserrat",sans-serif;font-weight:800;font-size:24px;line-height:32px;color:var(--yellow);
    text-shadow:2px 3px 0 rgba(0,0,0,.7);
  }
</style>
</head>
<body>
<main class="flyer">
  <div class="hero-graphic" role="img" aria-label="Chequered flag and speedometer dial artwork"></div>
  <div class="track-scene" role="img" aria-label="Racetrack straight with start line under stadium lights"></div>

  <div class="brand-mark"><span class="brand-name">VOLTA</span></div>

  <h1 class="title">
    <span class="line-1"><b>Volta</b></span>
    <span class="line-2"><b>Racing</b></span>
    <span class="line-3"><b>League</b></span>
  </h1>

  <p class="season season-kicker">NEW SEASON</p>
  <p class="season season-headline">JUST STARTING!!!</p>

  <p class="pitch">VERY POPULAR, CLEAN AND COMPETITIVE<br>ONLINE RACING LEAGUE, RUNNING FOR ITS 4TH SEASON<br>3 DIVISIONS CURRENTLY LOOKING TO KEEP GROWING!</p>

  <div class="invite">
    <svg class="chevrons" viewBox="0 0 84 34" aria-hidden="true">
      <g fill="#ffffff"><polygon points="0,0 14,0 28,17 14,34 0,34 14,17"/><polygon points="28,0 42,0 56,17 42,34 28,34 42,17"/><polygon points="56,0 70,0 84,17 70,34 56,34 70,17"/></g>
    </svg>
    <span class="invite-text">WHY NOT JOIN WITH A FRIEND?</span>
    <svg class="chevrons" viewBox="0 0 84 34" aria-hidden="true">
      <g fill="#ffffff"><polygon points="84,0 70,0 56,17 70,34 84,34 70,17"/><polygon points="56,0 42,0 28,17 42,34 56,34 42,17"/><polygon points="28,0 14,0 0,17 14,34 28,34 14,17"/></g>
    </svg>
  </div>

  <p class="race-times">RACE TIMES<br>MONDAYS, TUESDAYS,<br>AND WEDNESDAYS @ 8PM UK TIME</p>
  <p class="contact-note">MESSAGE BELOW FOR ANY QUESTIONS</p>
</main>
</body>
</html>
```